New cake shop needs a gorgeous website!

I need an easy to navigate and update (from my Mac - in layman's terms!) website for my new business - Crumb & Fern. This is a dietary friendly cake shop in Ponsonby, Auckland, New Zealand. We will be having Tarawhiti coffee (organic, fair-trade) Lumen Fizz range and specialty teas. Eat in, takeaway and delivery.
I will require you to upload and write if necessary, onto a program such as Pagecraft or similar.
I need a homepage, gallery page, price and ordering page (although the orders will be done via email/phone, no payments will be taken directly from the website) about us page, products and services page(this could incorporate the gallery maybe) a classes info page and a contact page.
My branding is very modern and clean. No vintage or french industrial is to be seen! We are sleek, with lots of white, black, charcoal grey and hot pink.
I will have photos to use in about 10 days, but I will upload some temporary images to start you off....
We also have a focus on 'a little bit good for you' and aim to make cakes that everyone can eat, whether they be gluten, dairy or egg intolerant or trying to lower the sugar in their diet.
A great design will be modern, exciting and convey a feel of luxury.
Please check out my pinterest page http://www.pinboardly.example/wrenbolt/coffee-cards-flyers-and-websites/
and feel free to use images from my instagram - fernbakenz.
Thanks!

```html
<!DOCTYPE html>
<html lang="en">
<head>
<meta charset="utf-8">
<title>Crumb &amp; Fern</title>
<link href="https://fonts.googleapis.com/css2?family=Raleway:wght@200;300;400;600&display=swap" rel="stylesheet">
<style>
  :root {
    --hot-pink: #e61f8c;
    --pink-veil: rgba(236, 40, 150, 0.82);
    --black: #0a0a0a;
    --charcoal: #1c1c1c;
    --white: #ffffff;
    --soft-white: #f4f4f4;
  }
  * { box-sizing: border-box; margin: 0; padding: 0; }
  html, body { width: 684px; height: 1200px; overflow: hidden; background: var(--white); }
  body { font-family: "Raleway", Arial, sans-serif; color: var(--white); position: relative; }

  .site-nav {
    position: absolute; top: 0; left: 0; width: 684px; height: 41px;
    background: var(--hot-pink);
    display: flex; align-items: center; justify-content: space-between;
    padding: 0 26px; font-size: 13px; font-weight: 400;
  }
  .site-nav .nav-group { display: flex; gap: 56px; }
  .brand { font-size: 21px; font-weight: 600; letter-spacing: 1px; text-transform: uppercase; }

  .hero {
    position: absolute; top: 41px; left: 0; width: 684px; height: 392px;
    background:
      radial-gradient(circle at 20% 30%, rgba(255,255,255,0.25), transparent 30%),
      radial-gradient(circle at 75% 70%, rgba(220,210,220,0.3), transparent 25%),
      linear-gradient(160deg, #5a0c12 0%, #b3172a 35%, #8a1020 60%, #3b2a30 100%);
  }
  .hero-title {
    position: absolute; top: 128px; width: 100%; text-align: center;
    font-size: 46px; font-weight: 200;
  }
  .hero-sub {
    position: absolute; top: 190px; width: 100%; text-align: center;
    font-size: 15px; font-weight: 300;
  }
  .btn {
    position: absolute; background: var(--hot-pink); color: var(--white);
    font-size: 15px; font-weight: 300; text-align: center; line-height: 30px; height: 30px;
  }
  .hero .btn { top: 310px; left: 296px; width: 92px; }

  .arrivals { position: absolute; top: 433px; left: 0; width: 684px; height: 308px; background: var(--black); }
  .tile { position: absolute; border: 2px solid var(--black); }
  .label-tile { position: absolute; display: flex; align-items: center; justify-content: center; font-size: 17px; font-weight: 400; }
  .caption { position: absolute; left: 4px; bottom: 4px; font-size: 9px; color: var(--white); }
  .see-more { color: var(--hot-pink); }

  .about {
    position: absolute; top: 741px; left: 0; width: 684px; height: 376px;
    background: linear-gradient(180deg, #c9a98e 0%, #8a6a4f 45%, #5e4330 100%);
  }
  .about-veil {
    position: absolute; top: 46px; left: 0; width: 684px; height: 272px;
    background: var(--pink-veil);
  }
  .about-copy {
    position: absolute; top: 82px; left: 100px; width: 484px;
    text-align: center; font-size: 15.5px; font-weight: 300; line-height: 1.45;
  }
  .about .btn { top: 335px; left: 288px; width: 108px; }

  .site-footer {
    position: absolute; top: 1117px; left: 0; width: 684px; height: 83px; background: var(--charcoal);
  }
  .footer-links {
    position: absolute; top: 38px; left: 58px; display: flex; gap: 30px; font-size: 10px; font-weight: 400;
  }
  .social { position: absolute; top: 36px; left: 614px; display: flex; gap: 6px; }
  .social span { width: 14px; height: 14px; border-radius: 50%; background: var(--white); display: block; }
  .copyright { position: absolute; top: 64px; width: 100%; text-align: center; font-size: 8px; color: #bbb; }
</style>
</head>
<body>
  <nav class="site-nav">
    <div class="nav-group"><span>About Us</span><span>Gallery</span></div>
    <div class="brand">Crumb &amp; Fern</div>
    <div class="nav-group"><span>Classes</span><span>Contact Us</span></div>
  </nav>

  <header class="hero" role="img" aria-label="Close-up photo of raspberries and chocolate truffles dusted with coconut">
    <h1 class="hero-title">A little bit good for you.</h1>
    <p class="hero-sub">Gluten free, dairy free &amp; low sugar</p>
    <div class="btn">Explore</div>
  </header>

  <section class="arrivals">
    <div class="label-tile" style="top:0;left:0;width:141px;height:144px;">New Arrivals</div>
    <div class="tile" role="img" aria-label="White chocolate lemon cake with edible flowers" style="top:0;left:141px;width:136px;height:144px;background:linear-gradient(150deg,#7a4a2a,#d9a24a 55%,#f2e6d0);">
      <span class="caption">White Chocolate Lemon Cake</span>
    </div>
    <div class="tile" role="img" aria-label="Round cake topped with berries" style="top:0;left:277px;width:136px;height:144px;background:linear-gradient(160deg,#f3eee8,#8a3d24 60%,#4a2314);"></div>
    <div class="tile" role="img" aria-label="Cake decorated with flower petals" style="top:0;left:413px;width:136px;height:144px;background:linear-gradient(140deg,#5b2a18,#c7752f 50%,#e2c79a);"></div>
    <div class="tile" role="img" aria-label="Berry topped cake on a plate" style="top:0;left:549px;width:135px;height:144px;background:linear-gradient(150deg,#e9e2dc,#a3262c 55%,#5b1a18);"></div>
    <div class="tile" role="img" aria-label="Layered naked cake with fresh flowers" style="top:144px;left:0;width:170px;height:164px;background:linear-gradient(170deg,#1a1a1a,#8c3b3b 45%,#d9c3a8);"></div>
    <div class="tile" role="img" aria-label="Meringue topped cake with caramel drizzle" style="top:144px;left:170px;width:168px;height:164px;background:linear-gradient(160deg,#f2efe8,#d49a3c 55%,#6a3a12);"></div>
    <div class="tile" role="img" aria-label="Chocolate cake decorated with orange and pink flowers" style="top:144px;left:338px;width:168px;height:164px;background:linear-gradient(150deg,#f3f0ec,#d2582a 45%,#4a2218);"></div>
    <div class="label-tile see-more" style="top:144px;left:506px;width:178px;height:164px;">See more</div>
  </section>

  <section class="about" role="img" aria-label="Photo of a bakery counter with trays of baking">
    <div class="about-veil"></div>
    <p class="about-copy">We specialise in visually attractive delicious cupcakes, cakes and coffees that are suitable for various diets incl gluten free, dairy free and low sugar. Crumb &amp; Fern also provides cakes for special events such as weddings, birthdays, christenings.</p>
    <div class="btn">Contact Us</div>
  </section>

  <footer class="site-footer">
    <div class="footer-links">
      <span>About Us</span><span>Gallery</span><span>Price</span><span>Ordering Page</span><span>Product &amp; Services</span><span>Classes Info</span><span>Contact Us</span>
    </div>
    <div class="social"><span></span><span></span></div>
    <p class="copyright">© 2014 Crumb &amp; Fern. All right reserved</p>
  </footer>
</body>
</html>
```